Online Cooking App Pitch Deck- (THIS IS NOT A FOOD BUSINESS OR FOOD SERVICE, NO FOOD PICTURES)

Project Goal:
Design a visually compelling pitch deck to be used for securing investment. Looking for the pitch deck to be about the design using shapes, colors, fonts and sizes. Must be creative yet simple and clean.
Color Palette:
https://palettrix.example/ff3800-ffe2db-fefefa-2d3e50-010b13

(We want most screens to use #FEFEFA)

This is the current pitch deck we need simplified and redesigned (USE TEXT IN THE GOOGLE LINK TO SHOW IN YOUR DESIGN):

https://slides.vornidex.example/deck/8QmTzR42kLpWx7nHa3Jv-cYdoeBtfGuqN/edit?share=link&uid=592031846720518390417&fmt=true&mode=true

Project is now guaranteed. Remember use the text in the google link in powerpoint design. Use a little more color not just the logo color. Do not use any pictures of food this is not food related business. We care more about style and design of shapes, text, color fonts.

Target Market(s)

Investors (venture capitalists, angel investors) interested in innovative technology solutions within the food industry.

Font styles to use
Serif
Sans Serif

Requirements
Nice to have
• Simple, abstract background non distracting but complementary.
Should not have
• No pictures

```html
<!DOCTYPE html>
<html lang="en">
<head>
<meta charset="utf-8">
<title>Whisk &amp; Sear — Investor Deck Overview</title>
<link rel="stylesheet" href="https://fonts.googleapis.com/css2?family=Montserrat:wght@300;400;600;700;800&display=swap">
<style>
  :root{
    --orange:#ff3800;
    --peach:#ffc3b2;
    --blush:#ffe2db;
    --paper:#fefefa;
    --slate:#2d3e50;
    --ink:#010b13;
    --pattern-a:#f3f3ef;
    --pattern-b:#eaeae6;
    --muted:#4a4f55;
  }
  *{box-sizing:border-box;margin:0;padding:0}
  html,body{width:1042px;height:1200px;overflow:hidden;background:#ffffff}
  body{position:relative;font-family:"Montserrat",Arial,sans-serif;color:var(--ink)}

  .slide{position:absolute;width:254px;height:143px;background:var(--paper);overflow:hidden;
    box-shadow:3px 4px 8px rgba(0,0,0,.22)}
  .col1{left:61px}.col2{left:394px}.col3{left:726px}
  .row1{top:34px}.row2{top:200px}.row3{top:366px}.row4{top:532px}
  .row5{top:698px}.row6{top:865px}.row7{top:1031px}

  .pattern{position:absolute;inset:0;background:linear-gradient(160deg,var(--pattern-a),var(--pattern-b) 50%,var(--pattern-a))}

  .tag,.brand{position:absolute;top:7px;font-size:4px;font-weight:700;z-index:2}
  .tag{left:9px}.brand{right:9px}
  .accent{color:var(--orange)}
  .foot{position:absolute;left:9px;bottom:5px;font-size:2.8px;font-weight:700;z-index:2}
  .pg{position:absolute;right:9px;bottom:5px;font-size:2.8px;font-weight:700;z-index:2}
  .pg::before{content:"";display:inline-block;width:6px;height:.5px;background:var(--orange);vertical-align:middle;margin-right:1px}

  .mark{position:absolute;width:54px;height:54px;border-radius:50%;background:var(--orange);top:45px;left:9px;z-index:1}
  .section-title{position:absolute;left:80px;top:49px;font-size:18.5px;font-weight:800;line-height:1.2;z-index:1}

  .utensil{position:absolute;background:var(--peach);border-radius:14px;z-index:1}

  .copy{position:absolute;right:9px;text-align:right;z-index:1}
  .label{font-size:5.5px;font-weight:700;margin-bottom:6px}
  .headline{font-size:11.5px;font-weight:700;line-height:1.3}
  .body{font-size:3.4px;line-height:1.5;color:var(--muted);margin-top:7px}

  /* cover */
  .cover-mark{top:40px;left:18px;width:62px;height:62px}
  .cover-title{position:absolute;left:105px;top:38px;font-size:20px;font-weight:800;line-height:1.3;letter-spacing:.3px;z-index:1}
  .cover-sub{position:absolute;left:105px;top:88px;font-size:7.8px;font-weight:300;line-height:1.45;z-index:1}

  .title-card{position:absolute;left:0;right:0;top:38px;text-align:center;z-index:1}
  .title-card .name{font-size:24px;font-weight:700}
  .title-card .name sup{font-size:5px;vertical-align:top;position:relative;top:4px}
  .title-card .lead{font-size:11.5px;font-weight:700;margin-top:3px}
  .title-card .motto{font-size:12px;font-weight:400;margin-top:4px}

  /* competitors */
  .comp-head{position:absolute;left:11px;top:19px;font-size:7px;font-weight:700}
  .comp{position:absolute;top:38px;width:64px;font-size:3.3px;line-height:1.45;color:var(--muted)}
  .comp .logo{display:block;text-align:center;font-size:6px;font-weight:700;color:var(--ink);margin-bottom:4px}
  .comp .val{position:absolute;top:64px;font-weight:700;color:var(--ink);white-space:nowrap}

  /* differentiators */
  .dark-panel{position:absolute;left:0;top:0;bottom:0;width:79px;background:var(--ink);color:var(--paper);padding:7px 10px}
  .dark-panel .tag{color:var(--paper)}
  .dark-panel h3{font-size:7px;font-weight:700;line-height:1.3;margin-top:11px}
  .dark-panel h4{font-size:4.6px;font-weight:700;line-height:1.45;margin-top:13px}
  .dark-panel p{font-size:3.3px;line-height:1.45;color:#b7b9bb;margin-top:2px}
  .dark-panel .foot{color:var(--paper)}
  .points{position:absolute;left:89px;right:9px;top:16px}
  .point{position:relative;padding-left:13px;margin-bottom:5px}
  .point svg{position:absolute;left:0;top:0;width:7px;height:7px}
  .point h5{font-size:3.8px;font-weight:700;color:var(--orange)}
  .point p{font-size:2.8px;line-height:1.45;color:var(--muted);margin-top:1px}
  .point b{color:var(--ink)}

  .demo-title{position:absolute;left:63px;top:68px;font-size:14px;font-weight:700;line-height:1.3;z-index:1}
  .device{position:absolute;left:112px;top:24px;width:74px;height:98px;border-radius:10px;
    background:linear-gradient(135deg,#2a2a2a,#0c0c0c);transform:rotate(-32deg) translate(10px,4px)}

  .team-label{position:absolute;left:9px;top:37px;font-size:5.5px;font-weight:700}
  .team-name{position:absolute;left:9px;top:52px;font-size:11px;font-weight:800}
  .team-role{position:absolute;left:9px;top:66px;font-size:8px;font-weight:400;color:var(--orange)}
  .team-bio{position:absolute;left:9px;top:86px;width:134px;font-size:3.3px;line-height:1.5;color:var(--muted)}
  .portrait{position:absolute;left:152px;top:35px;width:88px;height:88px;border-radius:50%;
    background:linear-gradient(160deg,#d9cfc4,#8b6a55 60%,#5a463a)}

  .fin-head{position:absolute;left:11px;top:17px;font-size:7px;font-weight:700}
  .fin-col{position:absolute;top:39px;width:56px}
  .fin-col .yr{font-size:8.5px;font-weight:700;color:var(--orange)}
  .fin-col .k{font-size:2.8px;font-weight:700;margin-top:3px}
  .fin-col .v{font-size:5.5px;font-weight:600;margin-top:4px;margin-bottom:5px}
</style>
</head>
<body>

<!-- 1 Cover -->
<section class="slide col1 row1">
  <div class="pattern" role="img" aria-label="Faint repeating brand pattern background"></div>
  <div class="mark cover-mark"></div>
  <h1 class="cover-title">INVESTOR<br>OVERVIEW</h1>
  <p class="cover-sub">THIS DOCUMENT EXISTS FOR<br>OUR FUTURE PARTNERS.</p>
  <div class="foot">Proprietary <span class="accent">and</span> Confidential</div>
</section>

<!-- 2 Title -->
<section class="slide col2 row1">
  <div class="pattern" role="img" aria-label="Faint repeating brand pattern background"></div>
  <div class="title-card">
    <div class="name">Whisk <span class="accent">&amp;</span> Sear<sup>TM</sup></div>
    <div class="lead">A New Cooking Platform</div>
    <div class="motto">Cook, <span class="accent">Learn,</span> Repeat</div>
  </div>
  <div class="foot">Proprietary <span class="accent">and</span> Confidential</div>
  <div class="pg">2</div>
</section>

<!-- 3 What is -->
<section class="slide col3 row1">
  <div class="tag">Cook, <span class="accent">Learn,</span> Repeat</div>
  <div class="brand">Whisk <span class="accent">&amp;</span> Sear</div>
  <div class="utensil" style="left:10px;top:40px;width:50px;height:80px" role="img" aria-label="Soft peach ladle illustration"></div>
  <div class="copy" style="top:36px;width:175px">
    <div class="headline accent" style="font-size:11px">What Is <span style="color:var(--ink)">Whisk</span> &amp; <span style="color:var(--ink)">Sear?</span></div>
    <p class="body">Whisk &amp; Sear is an online platform where home cooks learn live from chefs around the world, in small interactive classes built around real kitchens, real schedules and real skill growth.</p>
    <p class="body" style="margin-top:4px">Chefs host, teach and earn on their own terms, while students book, cook along and come back for more.</p>
  </div>
  <div class="foot">Proprietary <span class="accent">and</span> Confidential</div>
  <div class="pg">3</div>
</section>

<!-- 4 Consumer Insights -->
<section class="slide col1 row2">
  <div class="pattern" role="img" aria-label="Faint repeating brand pattern background"></div>
  <div class="tag">Cook, <span class="accent">Learn,</span> Repeat</div>
  <div class="brand">Whisk <span class="accent">&amp;</span> Sear</div>
  <div class="mark"></div>
  <h2 class="section-title">Consumer<br>Insights</h2>
  <div class="foot">Proprietary <span class="accent">and</span> Confidential</div>
  <div class="pg">4</div>
</section>

<!-- 5 Insight 1 -->
<section class="slide col2 row2">
  <div class="tag">Cook, <span class="accent">Learn,</span> Repeat</div>
  <div class="brand">Whisk <span class="accent">&amp;</span> Sear</div>
  <div class="utensil" style="left:9px;top:52px;width:60px;height:60px;border-radius:30px 30px 6px 30px" role="img" aria-label="Soft peach spoon illustration"></div>
  <div class="copy" style="top:37px;width:170px">
    <div class="label">Insight 1</div>
    <div class="headline">Growing Interest In<br><span class="accent">Virtual Cooking Classes</span></div>
    <p class="body">Consumers seeking alternatives, more choices, easier preference management, or simply a way to avoid crowded spaces are increasingly turning to online culinary education platforms. This trend is fueled by the desire to learn new cooking skills, explore different cuisines, and enjoy cooking as a leisure activity or a bonding experience with friends and family, even if remotely.</p>
  </div>
  <div class="foot">Proprietary <span class="accent">and</span> Confidential</div>
  <div class="pg">5</div>
</section>

<!-- 6 Insight 2 -->
<section class="slide col3 row2">
  <div class="tag">Cook, <span class="accent">Learn,</span> Repeat</div>
  <div class="brand">Whisk <span class="accent">&amp;</span> Sear</div>
  <div class="utensil" style="left:26px;top:40px;width:48px;height:80px" role="img" aria-label="Soft peach ladle illustration"></div>
  <div class="copy" style="top:37px;width:170px">
    <div class="label">Insight 2</div>
    <div class="headline">Demand For Interactive And<br><span class="accent">Personalized Experience</span></div>
    <p class="body">Consumers value interactive and personalized virtual cooking experiences. This includes live classes with real-time feedback from chefs, personalized meal planning, and customization options that cater to dietary restrictions or preferences. Platforms that offer these personalized interactions tend to be more popular.</p>
  </div>
  <div class="foot">Proprietary <span class="accent">and</span> Confidential</div>
  <div class="pg">6</div>
</section>

<!-- 7 Insight 3 -->
<section class="slide col1 row3">
  <div class="tag">Cook, <span class="accent">Learn,</span> Repeat</div>
  <div class="brand">Whisk <span class="accent">&amp;</span> Sear</div>
  <div class="utensil" style="left:9px;top:52px;width:62px;height:62px;border-radius:30px 6px 30px 30px" role="img" aria-label="Soft peach spoon illustration"></div>
  <div class="copy" style="top:37px;width:170px">
    <div class="label">Insight 3</div>
    <div class="headline">Global Cuisine<br><span class="accent">Exploration</span></div>
    <p class="body">There is a marked interest in exploring global cuisines through virtual cooking classes. Consumers are eager to learn about and experiment with dishes from different cultures, driven by a desire for new experiences and flavors. This trend is facilitated by the accessibility of virtual classes, which can connect chefs and culinary instructors from around the world with interested learners.</p>
  </div>
  <div class="foot">Proprietary <span class="accent">and</span> Confidential</div>
  <div class="pg">7</div>
</section>

<!-- 8 The Problem section -->
<section class="slide col2 row3">
  <div class="pattern" role="img" aria-label="Faint repeating brand pattern background"></div>
  <div class="tag">Cook, <span class="accent">Learn,</span> Repeat</div>
  <div class="brand">Whisk <span class="accent">&amp;</span> Sear</div>
  <div class="mark"></div>
  <h2 class="section-title">The<br>Problem</h2>
  <div class="foot">Proprietary <span class="accent">and</span> Confidential</div>
  <div class="pg">8</div>
</section>

<!-- 9 The Problem -->
<section class="slide col3 row3">
  <div class="tag">Cook, <span class="accent">Learn,</span> Repeat</div>
  <div class="brand">Whisk <span class="accent">&amp;</span> Sear</div>
  <div class="utensil" style="left:10px;top:40px;width:50px;height:80px" role="img" aria-label="Soft peach ladle illustration"></div>
  <div class="copy" style="top:53px;width:180px">
    <div class="headline">The<br><span class="accent">Problem</span></div>
    <p class="body">Learning to cook well is still locked behind costly schools, fixed schedules and one-way videos. Home cooks want feedback, not just footage, and most platforms give them no way to ask, adjust or connect.</p>
  </div>
  <div class="foot">Proprietary <span class="accent">and</span> Confidential</div>
  <div class="pg">9</div>
</section>

<!-- 10 Market Opportunity -->
<section class="slide col1 row4">
  <div class="pattern" role="img" aria-label="Faint repeating brand pattern background"></div>
  <div class="tag">Cook, <span class="accent">Learn,</span> Repeat</div>
  <div class="brand">Whisk <span class="accent">&amp;</span> Sear</div>
  <div class="mark"></div>
  <h2 class="section-title">Market<br>Opportunity</h2>
  <div class="foot">Proprietary <span class="accent">and</span> Confidential</div>
  <div class="pg">10</div>
</section>

<!-- 11 Market Insight 1 -->
<section class="slide col2 row4">
  <div class="tag">Cook, <span class="accent">Learn,</span> Repeat</div>
  <div class="brand">Whisk <span class="accent">&amp;</span> Sear</div>
  <div class="utensil" style="left:10px;top:43px;width:26px;height:78px;border-radius:4px 4px 13px 13px" role="img" aria-label="Soft peach spoon illustration"></div>
  <div class="copy" style="top:37px;width:200px">
    <div class="label">Insight 1</div>
    <div class="headline">Increasing Demand For<br><span class="accent">Healthier Home-cooked Meals</span></div>
    <p class="body">Busy households want to eat better at home but lack the time and confidence to plan it. Short live classes turn healthy cooking into a habit they can keep, one weeknight at a time.</p>
  </div>
  <div class="foot">Proprietary <span class="accent">and</span> Confidential</div>
  <div class="pg">11</div>
</section>

<!-- 12 Market Insight 2 -->
<section class="slide col3 row4">
  <div class="tag">Cook, <span class="accent">Learn,</span> Repeat</div>
  <div class="brand">Whisk <span class="accent">&amp;</span> Sear</div>
  <div class="utensil" style="left:26px;top:40px;width:48px;height:80px" role="img" aria-label="Soft peach ladle illustration"></div>
  <div class="copy" style="top:37px;width:170px">
    <div class="label">Insight 2</div>
    <div class="headline">Convenience And<br><span class="accent">Time-saving Solutions</span></div>
    <p class="body">Another key insight is the high demand for convenience and time-saving solutions, particularly among busy households and individuals with fast-paced lifestyles. Quick classes and smart prep guides fit real weeknights.</p>
  </div>
  <div class="foot">Proprietary <span class="accent">and</span> Confidential</div>
  <div class="pg">12</div>
</section>

<!-- 13 Current Solutions -->
<section class="slide col1 row5">
  <div class="pattern" role="img" aria-label="Faint repeating brand pattern background"></div>
  <div class="tag">Cook, <span class="accent">Learn,</span> Repeat</div>
  <div class="brand">Whisk <span class="accent">&amp;</span> Sear</div>
  <div class="mark" style="left:25px"></div>
  <h2 class="section-title" style="left:96px">Current<br>Solutions</h2>
  <div class="foot" style="left:1px">Proprietary <span class="accent">and</span> Confidential</div>
  <div class="pg">13</div>
</section>

<!-- 14 Competitors -->
<section class="slide col2 row5">
  <div class="tag">Cook, <span class="accent">Learn,</span> Repeat</div>
  <div class="brand">Whisk <span class="accent">&amp;</span> Sear</div>
  <h2 class="comp-head">Competitors</h2>
  <div class="comp" style="left:17px">
    <span class="logo">Lumaclass</span>
    Lumaclass, a leader in online prerecorded learning, offers celebrity-taught video courses across various subjects. Their high production value and renowned instructors have made them a powerhouse in the premium learning space.
    <span class="val" style="left:3px">Estimated Valuation: <span class="accent">$2.7B</span></span>
  </div>
  <div class="comp" style="left:95px">
    <span class="logo">Maison Platter</span>
    Maison Platter was a prominent player in the high-end kitchenware and cooking class space. They offered in-store shopping experiences with premium cookware and ingredients, alongside engaging cooking classes led by culinary professionals.
    <span class="val" style="left:3px">Estimated Valuation: <span class="accent">$50M</span></span>
  </div>
  <div class="comp" style="left:173px">
    <span class="logo accent">Hearthly</span>
    Hearthly, another player in the online culinary education space, provides in-person and online cooking classes with a focus on connecting users with local chefs. They offer a variety of class formats, from group courses to private chef experiences.
    <span class="val" style="left:3px">Estimated Valuation: <span class="accent">$2.6M</span></span>
  </div>
  <div class="foot">Proprietary <span class="accent">and</span> Confidential</div>
  <div class="pg">14</div>
</section>

<!-- 15 A Better Solution -->
<section class="slide col3 row5">
  <div class="pattern" role="img" aria-label="Faint repeating brand pattern background"></div>
  <div class="tag">Cook, <span class="accent">Learn,</span> Repeat</div>
  <div class="brand">Whisk <span class="accent">&amp;</span> Sear</div>
  <div class="mark"></div>
  <h2 class="section-title">A Better<br>Solution</h2>
  <div class="foot">Proprietary <span class="accent">and</span> Confidential</div>
  <div class="pg">15</div>
</section>

<!-- 16 Why we're different -->
<section class="slide col1 row6">
  <aside class="dark-panel">
    <div class="tag">Cook, <span class="accent">Learn,</span> Repeat</div>
    <h3>Why we’re<br>different</h3>
    <h4>Forget Gatekeepers, Unleash Passion: Whisk &amp; Sear Revolutionizes Culinary Education</h4>
    <p>The current culinary education landscape is dominated by limited options. Live classes open the door for everyone.</p>
    <div class="foot">Proprietary <span class="accent">and</span> Confidential</div>
  </aside>
  <div class="brand">Whisk <span class="accent">&amp;</span> Sear</div>
  <div class="points">
    <div class="point">
      <svg viewBox="0 0 10 10"><rect x=".5" y=".5" width="9" height="9" fill="none" stroke="#ff3800" stroke-width=".9"/><path d="M2.3 5.2l2 2 3.6-4.6" fill="none" stroke="#ff3800" stroke-width="1"/></svg>
      <h5>Anyone Can Host</h5>
      <p>Any passionate cook can open a class, set a schedule and share what they know with learners everywhere.</p>
    </div>
    <div class="point">
      <svg viewBox="0 0 10 10"><rect x=".5" y=".5" width="9" height="9" fill="none" stroke="#ff3800" stroke-width=".9"/><path d="M2.3 5.2l2 2 3.6-4.6" fill="none" stroke="#ff3800" stroke-width="1"/></svg>
      <h5>Unleash the Global Kitchen: Real-Time Learning Without Borders</h5>
      <p>Forget pre-recorded lessons and geographical limitations. Whisk &amp; Sear fosters a dynamic learning environment where real-time interaction breaks down barriers. Students can ask questions, receive personalized feedback, and connect with instructors in the moment.</p>
      <p>Imagine connecting with a street food vendor in Bangkok for a live Pad Thai masterclass, or learning the secrets of Neapolitan pizza from a Neapolitan chef, all from the comfort of your own kitchen.</p>
    </div>
    <div class="point">
      <svg viewBox="0 0 10 10"><rect x=".5" y=".5" width="9" height="9" fill="none" stroke="#ff3800" stroke-width=".9"/><path d="M2.3 5.2l2 2 3.6-4.6" fill="none" stroke="#ff3800" stroke-width="1"/></svg>
      <h5>Empowering Chefs, Building Sustainable Income</h5>
      <p>Whisk &amp; Sear empowers chefs to build a thriving online business.</p>
      <p><b>Monetize Your Expertise:</b> Chefs can set their own prices for classes, consultations, and workshops.</p>
      <p><b>Leverage Existing Audience:</b> Chefs can bring their social following to their classes, reaching a wider audience.</p>
      <p><b>Flexible Income Streams:</b> Classes, tips and guides add up month by month.</p>
    </div>
  </div>
  <div class="pg">16</div>
</section>

<!-- 17 Our Demo -->
<section class="slide col2 row6">
  <div class="tag">Cook, <span class="accent">Learn,</span> Repeat</div>
  <div class="brand">Whisk <span class="accent">&amp;</span> Sear</div>
  <div class="utensil" style="left:10px;top:40px;width:50px;height:80px" role="img" aria-label="Soft peach ladle illustration"></div>
  <h2 class="demo-title">Our<br><span class="accent">Demo</span></h2>
  <div class="device" role="img" aria-label="Smartphone showing the app demo screen"></div>
  <div class="foot">Proprietary <span class="accent">and</span> Confidential</div>
  <div class="pg">17</div>
</section>

<!-- 19 The Team section -->
<section class="slide col3 row6">
  <div class="pattern" role="img" aria-label="Faint repeating brand pattern background"></div>
  <div class="tag">Cook, <span class="accent">Learn,</span> Repeat</div>
  <div class="brand">Whisk <span class="accent">&amp;</span> Sear</div>
  <div class="mark"></div>
  <h2 class="section-title">The<br>Team</h2>
  <div class="foot">Proprietary <span class="accent">and</span> Confidential</div>
  <div class="pg">19</div>
</section>

<!-- 20 Team member -->
<section class="slide col1 row7">
  <div class="tag">Cook, <span class="accent">Learn,</span> Repeat</div>
  <div class="brand">Whisk <span class="accent">&amp;</span> Sear</div>
  <div class="team-label">The Team</div>
  <h2 class="team-name">DELPHINE OKORO</h2>
  <div class="team-role">Founder &amp; CEO</div>
  <p class="team-bio">Delphine has spent fifteen years building consumer products at the edge of food and technology. She leads product, partnerships and the chef community, and started Whisk &amp; Sear after teaching her first live class from a tiny home kitchen.</p>
  <div class="portrait" role="img" aria-label="Portrait photo of the founder and CEO"></div>
  <div class="foot">Proprietary <span class="accent">and</span> Confidential</div>
  <div class="pg">20</div>
</section>

<!-- 21 Revenue Model -->
<section class="slide col2 row7">
  <div class="pattern" role="img" aria-label="Faint repeating brand pattern background"></div>
  <div class="tag">Cook, <span class="accent">Learn,</span> Repeat</div>
  <div class="brand">Whisk <span class="accent">&amp;</span> Sear</div>
  <div class="mark"></div>
  <h2 class="section-title">Revenue<br>Model</h2>
  <div class="foot">Proprietary <span class="accent">and</span> Confidential</div>
  <div class="pg">21</div>
</section>

<!-- 23 Financial Projections -->
<section class="slide col3 row7">
  <div class="tag">Cook, <span class="accent">Learn,</span> Repeat</div>
  <div class="brand">Whisk <span class="accent">&amp;</span> Sear</div>
  <h2 class="fin-head">Financial Projections.</h2>
  <div class="fin-col" style="left:10px">
    <div class="yr">2024</div>
    <div class="k">User Growth</div><div class="v">2,000</div>
    <div class="k">Marketing &amp; Ad’s</div><div class="v">$30,000.00</div>
    <div class="k">Revenue</div><div class="v">$X00,000.00</div>
  </div>
  <div class="fin-col" style="left:70px">
    <div class="yr">2025</div>
    <div class="k">User Growth</div><div class="v">12,000</div>
    <div class="k">Marketing &amp; Ad’s</div><div class="v">$120,000.00</div>
    <div class="k">Revenue</div><div class="v">$2,X00,000.00</div>
  </div>
  <div class="fin-col" style="left:130px">
    <div class="yr">2026</div>
    <div class="k">User Growth</div><div class="v">22,000</div>
    <div class="k">Marketing &amp; Ad’s</div><div class="v">$120,000.00</div>
    <div class="k">Revenue</div><div class="v">$10,000,000.00</div>
  </div>
  <div class="fin-col" style="left:190px">
    <div class="yr">2027</div>
    <div class="k">User Growth</div><div class="v">30,000</div>
    <div class="k">Marketing &amp; Ad’s</div><div class="v">$150,000.00</div>
    <div class="k">Revenue</div><div class="v">$25,000,000.00</div>
  </div>
  <div class="foot">Proprietary <span class="accent">and</span> Confidential</div>
  <div class="pg">23</div>
</section>

</body>
</html>
```